"Drink Champagne and Dance on the Table" sort of business card needed!

We throw events, weddings, engagement parties, baby showers and the sort of end of year corporate events that people remember long after the glitter has settled - the sort of events that make you stand still and say wow when you walk in and then make you want to "Drink Champagne and Dance on the Tables"

We have a great logo with heaps of potential and need a business card that just screams creative professionals!

We are based in Auckland, NZ and are priced at the Premium end of the market were there are around 10 other main competitors. We need to stand out and make a strong statement about who we are!

Our Business Card will be one of the few items that we print out so are fully prepared to invest in a premium print job.

We really love our logo and think it has heaps of potential! Its ok if you would like to manipulate it (maybe put it on an angle, or use the circle element on its own?).

Black and Gold is very striking, but its very done in our market so we would like to avoid a solid black background please

We have done a bit of an inspiration document to give you an idea of the sort of look and feel we are hoping to achieve.

Target Market(s)

Woman aged 30 - 45 with an income bracket of $70k +

Industry/Entity Type

Event Planning

Contact Information for Business Card

Marnie
hello@fennwhistle.co.nz
www.fennwhistle.co.nz
02739418207

Number of Pages Required

5+ page

Requirements
Must have
• Vibrant colours and design (we love the vibrant pink and gold in the inspiration file)
• We would love to see some colour and creativity (although the black and gold is very striking). Because we are doing such minimal print work I am happy for the cards to be a little more expensive so if you want to use cut outs, rounded corners, gold foil, non standard size etc I am happy for that too. I really want the wow factor.
Nice to have
• We would like the design to be double sided.
Should not have
• The logo colour changed
• Use of Purple or Green or solid black background.
• Wedding Photos!

```html
<!DOCTYPE html>
<html lang="en">
<head>
<meta charset="utf-8">
<title>Fenn and Whistle – Business Card</title>
<link href="https://fonts.googleapis.com/css2?family=Arimo:ital,wght@0,400;1,400&display=swap" rel="stylesheet">
<style>
  :root {
    --backdrop: #ece8e2;
    --gold-deep: #b8853c;
    --gold-mid: #d3a95c;
    --gold-soft: #e6cf9f;
    --frost: #ebe8e2;
    --frost-edge: #f4f2ee;
    --bronze: #8c5a1e;
    --ink-light: #fffaf0;
    --ink-soft: #fbeedd;
  }
  * { margin: 0; padding: 0; box-sizing: border-box; }
  html, body {
    width: 1200px;
    height: 969px;
    overflow: hidden;
    background: var(--backdrop);
    font-family: "Arimo", Arial, sans-serif;
  }
  .canvas {
    position: relative;
    width: 1200px;
    height: 969px;
  }
  .business-card {
    position: absolute;
    left: 160px;
    top: 234px;
    width: 880px;
    height: 500px;
    border-radius: 26px;
    overflow: hidden;
    background: linear-gradient(100deg,
      var(--gold-deep) 0%,
      var(--gold-mid) 30%,
      var(--gold-soft) 52%,
      var(--frost) 72%,
      var(--frost-edge) 100%);
    box-shadow: 0 18px 40px rgba(90, 60, 20, 0.18);
  }
  .contact-name {
    position: absolute;
    left: 48px;
    top: 40px;
    font-size: 30px;
    color: var(--ink-light);
  }
  .contact-email {
    position: absolute;
    left: 48px;
    top: 86px;
    font-size: 20px;
    font-style: italic;
    color: var(--ink-soft);
  }
  .contact-line {
    position: absolute;
    left: 48px;
    display: flex;
    align-items: center;
    gap: 12px;
    font-size: 20px;
    letter-spacing: 0.5px;
    color: var(--ink-soft);
  }
  .contact-line.phone { top: 386px; }
  .contact-line.web { top: 424px; }
  .contact-icon { width: 20px; height: 20px; flex: none; }
  .brand-ring {
    position: absolute;
    left: 336px;
    top: 8px;
    width: 486px;
    height: 486px;
  }
  .brand-lockup {
    position: absolute;
    left: 399px;
    top: 290px;
    width: 360px;
    text-align: center;
    color: var(--bronze);
  }
  .brand-name {
    font-size: 38px;
    line-height: 1;
    white-space: nowrap;
  }
  .brand-tagline {
    margin-top: 12px;
    display: flex;
    align-items: center;
    justify-content: center;
    gap: 10px;
    font-size: 13px;
    letter-spacing: 3px;
  }
  .brand-tagline .rule {
    width: 40px;
    height: 1.5px;
    background: var(--bronze);
  }
</style>
</head>
<body>
<main class="canvas">
  <section class="business-card">
    <h1 class="contact-name">Marnie</h1>
    <p class="contact-email">hello@fennwhistle.co.nz</p>

    <p class="contact-line phone">
      <svg class="contact-icon" viewBox="0 0 24 24" aria-hidden="true">
        <path fill="#fbeedd" d="M6.6 10.8a15.1 15.1 0 0 0 6.6 6.6l2.2-2.2a1 1 0 0 1 1-.25 11.4 11.4 0 0 0 3.6.57 1 1 0 0 1 1 1V20a1 1 0 0 1-1 1A17 17 0 0 1 3 4a1 1 0 0 1 1-1h3.5a1 1 0 0 1 1 1c0 1.25.2 2.45.57 3.57a1 1 0 0 1-.25 1z"/>
      </svg>
      02739418207
    </p>
    <p class="contact-line web">
      <svg class="contact-icon" viewBox="0 0 24 24" aria-hidden="true">
        <circle cx="12" cy="12" r="9.5" fill="none" stroke="#fbeedd" stroke-width="2"/>
        <path d="M2.5 12h19M12 2.5c3 3 3 16 0 19M12 2.5c-3 3-3 16 0 19" fill="none" stroke="#fbeedd" stroke-width="1.6"/>
      </svg>
      www.fennwhistle.co.nz
    </p>

    <svg class="brand-ring" viewBox="0 0 486 486" aria-hidden="true">
      <circle cx="243" cy="243" r="232" fill="none" stroke="#8c5a1e" stroke-width="9"/>
    </svg>

    <div class="brand-lockup">
      <p class="brand-name">Fenn and Whistle</p>
      <p class="brand-tagline"><span class="rule"></span>WEDDINGS &amp; EVENTS<span class="rule"></span></p>
    </div>
  </section>
</main>
</body>
</html>
```